Business Card Design Project

Name: Kunle O. Edet
Designation: Partner
Address: QRM Building, 14 Harmony Close, P.O. Box 58314, Victoria Island Lagos, Nigeria
Tel: +234 1 7395162
mobile: +234 1 7061527394
Email: koedet@larkmoorassociates.com
website www.larkmoorassociates.com

```html
<!DOCTYPE html>
<html lang="en">
<head>
<meta charset="UTF-8">
<title>Kunle O. Edet — Business Card</title>
<link rel="stylesheet" href="https://fonts.googleapis.com/css2?family=Josefin+Sans:wght@600&family=Ubuntu:wght@400;500&display=swap">
<style>
  :root {
    --backdrop: #5c0010;
    --silver-edge: #a7adbb;
    --silver-mid: #dde0e6;
    --silver-light: #fafbfc;
    --ink: #3e4556;
    --icon: #5d6374;
    --band: #000000;
    --brand: #d6d9df;
    --brand-mark: #c3c7cf;
  }
  * { margin: 0; padding: 0; box-sizing: border-box; }
  html, body {
    width: 1200px;
    height: 960px;
    overflow: hidden;
    background: var(--backdrop);
  }
  .card {
    position: absolute;
    left: 60px;
    top: 156px;
    width: 1078px;
    height: 646px;
    border-radius: 84px;
    overflow: hidden;
    background: linear-gradient(90deg, var(--silver-edge) 0%, var(--silver-mid) 28%, var(--silver-light) 55%, var(--silver-mid) 80%, var(--silver-edge) 100%);
    color: var(--ink);
  }
  .holder-name {
    position: absolute;
    top: 72px;
    left: 0;
    width: 100%;
    text-align: center;
    font-family: "Josefin Sans", sans-serif;
    font-weight: 600;
    font-size: 66px;
    line-height: 1;
    letter-spacing: 0.05em;
    text-transform: uppercase;
  }
  .holder-role {
    position: absolute;
    top: 166px;
    left: 0;
    width: 100%;
    text-align: center;
    font-family: "Josefin Sans", sans-serif;
    font-weight: 600;
    font-size: 34px;
    line-height: 1;
    letter-spacing: 0.12em;
    text-transform: uppercase;
  }
  .brand-band {
    position: absolute;
    top: 222px;
    left: 0;
    width: 100%;
    height: 170px;
    background: var(--band);
  }
  .brand-dot {
    position: absolute;
    left: 164px;
    top: 15px;
    width: 140px;
    height: 140px;
    border-radius: 50%;
    background: var(--brand-mark);
  }
  .brand-name {
    position: absolute;
    left: 420px;
    width: 364px;
    top: 40px;
    text-align: right;
    font-family: "Ubuntu", sans-serif;
    font-weight: 500;
    color: var(--brand);
    line-height: 1;
  }
  .brand-name .brand-main { display: block; font-size: 56px; }
  .brand-name .brand-sub { display: block; font-size: 26px; margin-top: 4px; }
  .contact-row {
    position: absolute;
    height: 44px;
    display: flex;
    align-items: center;
    font-family: "Ubuntu", sans-serif;
    font-weight: 400;
    white-space: nowrap;
  }
  .contact-row svg { flex: none; fill: var(--icon); }
  .contact-row .icon-slot { width: 66px; display: flex; justify-content: flex-start; }
  .contact-address { left: 84px; top: 422px; font-size: 23px; }
  .contact-address .icon-slot { width: 66px; }
  .contact-tel { left: 80px; top: 490px; font-size: 28px; }
  .contact-mobile { left: 80px; top: 562px; font-size: 28px; }
  .contact-tel .icon-slot, .contact-mobile .icon-slot { width: 70px; }
  .contact-email { left: 504px; top: 490px; font-size: 27px; }
  .contact-web { left: 504px; top: 562px; font-size: 27px; }
  .contact-email .icon-slot, .contact-web .icon-slot { width: 92px; }
</style>
</head>
<body>
  <div class="card">
    <h1 class="holder-name">Kunle O. Edet</h1>
    <p class="holder-role">Partner</p>

    <div class="brand-band">
      <div class="brand-dot"></div>
      <p class="brand-name">
        <span class="brand-main">Larkmoor</span>
        <span class="brand-sub">Associates</span>
      </p>
    </div>

    <div class="contact-row contact-address">
      <span class="icon-slot">
        <svg width="34" height="44" viewBox="0 0 34 44" aria-hidden="true">
          <rect x="6" y="1" width="27" height="42" rx="2"/>
          <g fill="#eef0f3">
            <rect x="2" y="6" width="8" height="3" rx="1.5"/>
            <rect x="2" y="14" width="8" height="3" rx="1.5"/>
            <rect x="2" y="22" width="8" height="3" rx="1.5"/>
            <rect x="2" y="30" width="8" height="3" rx="1.5"/>
            <rect x="2" y="38" width="8" height="3" rx="1.5"/>
          </g>
        </svg>
      </span>
      <span>QRM Building, 14 Harmony Close, P.O. Box 58314, Victoria Island Lagos, Nigeria</span>
    </div>

    <div class="contact-row contact-tel">
      <span class="icon-slot">
        <svg width="44" height="44" viewBox="0 0 24 24" aria-hidden="true">
          <path d="M6.6 10.8c1.4 2.8 3.8 5.1 6.6 6.6l2.2-2.2c.3-.3.7-.4 1-.2 1.1.4 2.3.6 3.6.6.6 0 1 .4 1 1V20c0 .6-.4 1-1 1C10.6 21 3 13.4 3 4c0-.6.4-1 1-1h3.5c.6 0 1 .4 1 1 0 1.3.2 2.5.6 3.6.1.3 0 .7-.2 1L6.6 10.8z"/>
        </svg>
      </span>
      <span>+234 1 7395162</span>
    </div>

    <div class="contact-row contact-mobile">
      <span class="icon-slot">
        <svg width="26" height="46" viewBox="0 0 26 46" aria-hidden="true">
          <rect x="1" y="1" width="24" height="44" rx="5"/>
          <rect x="5" y="7" width="16" height="22" rx="1" fill="#eef0f3"/>
          <circle cx="13" cy="37" r="3" fill="#eef0f3"/>
        </svg>
      </span>
      <span>+234 1 7061527394</span>
    </div>

    <div class="contact-row contact-email">
      <span class="icon-slot">
        <svg width="50" height="32" viewBox="0 0 50 32" aria-hidden="true">
          <rect x="0" y="0" width="50" height="32"/>
          <path d="M2 2 L25 19 L48 2" fill="none" stroke="#eef0f3" stroke-width="2.5"/>
          <path d="M2 30 L19 15 M48 30 L31 15" fill="none" stroke="#eef0f3" stroke-width="2"/>
        </svg>
      </span>
      <span>koedet@larkmoorassociates.com</span>
    </div>

    <div class="contact-row contact-web">
      <span class="icon-slot">
        <svg width="40" height="40" viewBox="0 0 40 40" aria-hidden="true">
          <circle cx="20" cy="20" r="19"/>
          <g fill="none" stroke="#eef0f3" stroke-width="1.8">
            <ellipse cx="20" cy="20" rx="8" ry="19"/>
            <line x1="20" y1="1" x2="20" y2="39"/>
            <line x1="1" y1="20" x2="39" y2="20"/>
            <path d="M4 10 H36 M4 30 H36"/>
          </g>
        </svg>
      </span>
      <span>www.larkmoorassociates.com</span>
    </div>
  </div>
</body>
</html>
```